Luxury Brand Real Estate For Sale sign

**Update** I've added some examples from the internet of other signs that have a look similar to what I would like to see. I do not want my personal name in the sign. And the word FOR SALE Does not need to be so large - it can be more subtle.
I want to create a Real Estate for sale sign for my company that will be used for luxury/higher end real estate listings. I’m sharing my business card as well as a logo with new teal color to show what we're moving towards: we’re using Teal, white, black and gold.
Hoping the sign is simple, sophisticated and eye catching.
The sign should be 24" wide by 30" tall including the company name: Harbor Crest Realty Group and our logo, office phone number 727-555-0148 and website www.hcrgexample.com the words "For Sale"
Optional to add this e-mail address info@hcrgexample.com to the sign
Target Market(s)
Luxury home buyers
Industry/Entity Type
Real Estate
Look and feel

```html
<!DOCTYPE html>
<html lang="en">
<head>
<meta charset="utf-8">
<title>Harbor Crest Realty Group – For Sale Sign</title>
<link rel="stylesheet" href="https://fonts.googleapis.com/css2?family=Bebas+Neue&family=Montserrat:wght@500;600&display=swap">
<style>
  :root {
    --backdrop: #d4d4d4;
    --sign-white: #ffffff;
    --teal: #168783;
    --charcoal: #4b4c4e;
    --gold: #c5a253;
  }
  * { box-sizing: border-box; margin: 0; padding: 0; }
  html, body {
    width: 1200px;
    height: 1200px;
    overflow: hidden;
    background: var(--backdrop);
  }
  /* 24 x 30 portrait sign */
  .sign {
    position: absolute;
    left: 240px;
    top: 150px;
    width: 720px;
    height: 900px;
    background: var(--sign-white);
  }
  .sign-header {
    position: absolute;
    left: 0;
    top: 0;
    width: 100%;
    height: 230px;
    display: flex;
    align-items: center;
    justify-content: center;
    gap: 22px;
  }
  .brand-square {
    width: 64px;
    height: 64px;
    background: var(--teal);
    flex: none;
  }
  .brand-name {
    font-family: "Montserrat", sans-serif;
    font-weight: 600;
    font-size: 26px;
    letter-spacing: 0.5px;
    color: var(--teal);
    text-transform: uppercase;
    white-space: nowrap;
  }
  .header-rule {
    position: absolute;
    left: 0;
    top: 230px;
    width: 100%;
    height: 10px;
    background: var(--teal);
  }
  .header-rule-accent {
    position: absolute;
    left: 0;
    top: 246px;
    width: 100%;
    height: 3px;
    background: var(--gold);
  }
  .headline {
    position: absolute;
    left: 0;
    top: 340px;
    width: 100%;
    text-align: center;
    font-family: "Bebas Neue", sans-serif;
    font-weight: 400;
    font-size: 130px;
    line-height: 1;
    letter-spacing: 4px;
    color: var(--charcoal);
  }
  .divider {
    position: absolute;
    left: 320px;
    top: 500px;
    width: 80px;
    height: 3px;
    background: var(--gold);
  }
  .phone {
    position: absolute;
    left: 0;
    top: 535px;
    width: 100%;
    text-align: center;
    font-family: "Bebas Neue", sans-serif;
    font-size: 104px;
    line-height: 1;
    letter-spacing: 3px;
    color: var(--teal);
  }
  .sign-footer {
    position: absolute;
    left: 0;
    bottom: 0;
    width: 100%;
    height: 130px;
    background: var(--teal);
    border-top: 5px solid var(--gold);
    display: flex;
    align-items: center;
    justify-content: center;
  }
  .website {
    font-family: "Montserrat", sans-serif;
    font-weight: 500;
    font-size: 32px;
    letter-spacing: 3px;
    color: var(--sign-white);
  }
</style>
</head>
<body>
  <main class="sign">
    <header class="sign-header">
      <div class="brand-square"></div>
      <div class="brand-name">Harbor Crest Realty Group</div>
    </header>
    <div class="header-rule"></div>
    <div class="header-rule-accent"></div>
    <h1 class="headline">FOR SALE</h1>
    <div class="divider"></div>
    <p class="phone">727-555-0148</p>
    <footer class="sign-footer">
      <span class="website">www.hcrgexample.com</span>
    </footer>
  </main>
</body>
</html>
```